Dog care service needs business card design

Our company is Paws Harbour. We provide care for dogs while their owners are away, either through home visits or a holiday stay in the homes of carefully selected minders. Our existing website & Chatterbook cover should provide all the colour cues for our business cards - namely blues, blondes and grey. We have an existing logo (provided).

www.pawsharbourcare.example.au
www.facebook.com/pawsharbourcareau

We wish to clearly communicate our three areas of service "dog minding, home visits, dog walking".

We would like to have the files ready for upload to Printlyne (or similar) for immediate printing.

Target Market(s)

Dog owners who love their dogs like family

Industry/Entity Type

Business

Contact Information for Business Card

Paws Harbour
Ph: 0417 358 904

Font styles to use
Sans Serif

Colors
33a6d7
3176b5

Requirements
Must have
• Logo
• Telephone number
• website
• "Dog minding, home visits, dog walking"
Should not have
• any additional illustrations beyond the logo.

```html
<!DOCTYPE html>
<html lang="en">
<head>
<meta charset="utf-8">
<title>Paws Harbour – Business Card</title>
<link rel="stylesheet" href="https://fonts.googleapis.com/css2?family=Montserrat:wght@700&family=Arimo:wght@400&display=swap">
<style>
  :root {
    --brand-blue: #3176b5;
    --sky-blue: #33a6d7;
    --ink: #2b3a4a;
    --paper: #ffffff;
    --backdrop: #e6e8eb;
    --pale-blue: #8cc6e6;
  }
  * { box-sizing: border-box; margin: 0; padding: 0; }
  html, body {
    width: 1200px; height: 800px; overflow: hidden;
    background: var(--backdrop);
  }
  .sheet {
    width: 1200px; height: 800px;
    display: flex; align-items: center; justify-content: center; gap: 40px;
  }
  .card {
    width: 540px; height: 309px;
    position: relative; overflow: hidden;
    box-shadow: 0 6px 18px rgba(0,0,0,0.18);
  }

  /* Front */
  .card--front {
    background: var(--brand-blue);
    display: flex; align-items: center; justify-content: center;
  }
  .logo-plate {
    background: var(--paper);
    border-radius: 60px;
    padding: 26px 44px 22px;
    display: flex; flex-direction: column; align-items: center;
  }
  .brand {
    display: flex; align-items: center; gap: 14px;
  }
  .brand__dot {
    width: 44px; height: 44px; border-radius: 50%;
    background: var(--sky-blue);
  }
  .brand__name {
    font-family: "Montserrat", sans-serif; font-weight: 700;
    color: var(--ink); line-height: 1;
  }
  .card--front .brand__name { font-size: 40px; }
  .brand__tagline {
    font-family: "Montserrat", sans-serif; font-weight: 700;
    font-size: 11px; letter-spacing: 4px;
    color: var(--sky-blue); margin-top: 8px; padding-left: 58px;
  }

  /* Back */
  .card--back { background: var(--paper); }
  .card--back .brand { position: absolute; top: 34px; left: 0; right: 0; justify-content: center; gap: 10px; }
  .card--back .brand__dot { width: 30px; height: 30px; }
  .card--back .brand__name { font-size: 26px; }
  .card--back .brand__tagline {
    position: absolute; top: 66px; left: 0; right: 0; text-align: center;
    font-size: 8px; letter-spacing: 3px; padding-left: 40px;
  }
  .contact {
    position: absolute; top: 112px; left: 150px;
    list-style: none;
    font-family: "Arimo", sans-serif; font-size: 18px; color: var(--brand-blue);
  }
  .contact li { display: flex; align-items: center; gap: 10px; margin-bottom: 14px; }
  .contact__bullet { width: 7px; height: 7px; background: var(--sky-blue); border-radius: 1px; }
  .services-band {
    position: absolute; left: 0; right: 0; top: 196px; height: 44px;
    background: var(--brand-blue);
    border-top: 4px solid var(--sky-blue);
    display: flex; align-items: center; padding-left: 40px;
    font-family: "Arimo", sans-serif; font-size: 22px; color: var(--paper);
  }
  .services-rule {
    position: absolute; left: 0; right: 0; top: 248px; height: 3px;
    background: var(--pale-blue);
  }
</style>
</head>
<body>
  <main class="sheet">
    <section class="card card--front" aria-label="Card front">
      <div class="logo-plate">
        <div class="brand">
          <span class="brand__dot"></span>
          <span class="brand__name">Paws Harbour</span>
        </div>
        <span class="brand__tagline">PET SERVICES</span>
      </div>
    </section>

    <section class="card card--back" aria-label="Card back">
      <div class="brand">
        <span class="brand__dot"></span>
        <span class="brand__name">Paws Harbour</span>
      </div>
      <span class="brand__tagline">PET SERVICES</span>
      <ul class="contact">
        <li><span class="contact__bullet"></span>0417 358 904</li>
        <li><span class="contact__bullet"></span>www.pawsharbourcare.example.au</li>
      </ul>
      <div class="services-band">Dog minding, home visits, dog walking</div>
      <div class="services-rule"></div>
    </section>
  </main>
</body>
</html>
```